Australian White Sheep Brochure

I need a brochure that is catchy to the eye and modern for the agricultural field for KLMRN. The Australian White Sheep (a hair sheep) is debuting in the US for the first time this October on Bricklow Farm. Emphasis for the end consumer is on meat quality (healthier/more pleasing to the American palate) versus existing breeds already in the US..... higher omega 3s, increased intramuscular fat, and lower fat melting points with a very mild flavor. For lamb/sheep producers, Australian Whites are hardy and have higher fleshing ability with lower inputs. Lots of research has gone into creating a superior meat producing animal similar to that of Wagyu Beef. The purpose of this brochure is to promote the breed to sheep producers of its benefits to the end consumer. Information of the breed can be found at www.PelmoraRidgeNet.com and www.quenbrook.com.au

Target Market(s)

Livestock breeders and producers

Font styles to use
Serif
Sans Serif

Colors

Designer to choose colors to be used in the design.

Requirements
Must have
• Summary of the information on the website www.PelmoraRidgeNet.com. It needs to include KLMRN logo and somewhere give credit to Bricklow Farm as the importer of the breed from Australia to the US.
Nice to have
• Credit/reference to Quenbrook Farm and use their logo somewhere as well that can be found here http://www.quenbrook.com.au/

```html
<!DOCTYPE html>
<html lang="en">
<head>
<meta charset="utf-8">
<title>Australian White Brochure Spread</title>
<link href="https://fonts.googleapis.com/css2?family=Lato:wght@300;400;700;900&display=swap" rel="stylesheet">
<style>
  :root{
    --navy:#3a4585;
    --navy-deep:#2c3670;
    --red:#c8202f;
    --red-deep:#8e1420;
    --rust:#b9583f;
    --paper:#e9e9f3;
    --white:#ffffff;
    --grass:#7d8f5a;
    --fleece:#d9d2c4;
    --stone:#a89c8a;
    --meat:#d9a9a4;
  }
  *{margin:0;padding:0;box-sizing:border-box}
  html,body{width:1200px;height:789px;overflow:hidden;background:#2a2a2a}
  body{font-family:'Lato',sans-serif}
  .spread{position:relative;width:1200px;height:789px;display:flex}
  .page{position:relative;width:600px;height:789px;overflow:hidden}
  .page-bg{position:absolute;inset:0}
  .photo{position:absolute;border:3px solid var(--white);border-radius:12px}
  .photo-column{position:absolute;background:linear-gradient(180deg,var(--red),var(--red-deep));border-radius:26px}

  /* left page */
  .page--left .kicker{position:absolute;left:40px;top:42px;color:var(--rust);font-weight:300;font-size:28px}
  .page--left .title-bold{position:absolute;left:40px;top:74px;color:var(--white);font-weight:900;font-size:48px;line-height:1}
  .page--left .title-light{position:absolute;left:40px;top:124px;color:var(--white);font-weight:300;font-size:46px;line-height:1}
  .page--left .intro{position:absolute;left:40px;top:192px;width:370px;color:var(--white);font-size:10.5px;line-height:1.45}
  .page--left .intro p+p{margin-top:9px}
  .brand-mark{position:absolute;left:360px;top:700px;display:flex;align-items:center;gap:8px;color:var(--white);font-weight:900;font-size:22px}
  .brand-mark span.square{width:16px;height:16px;background:var(--red)}

  /* right page */
  .page--right .heading-bold{position:absolute;left:70px;top:120px;color:var(--white);font-weight:900;font-size:46px;line-height:1}
  .page--right .heading-light{position:absolute;left:70px;top:168px;color:var(--white);font-weight:300;font-size:46px;line-height:1}
  .page--right .standards{position:absolute;left:70px;top:240px;width:300px;color:var(--white);font-size:10.5px;line-height:1.45}
  .page--right .standards p+p{margin-top:8px}
  .rams-title{position:absolute;left:36px;top:548px;color:var(--red);font-weight:900;font-size:62px;line-height:1}
  .rams-text{position:absolute;left:36px;top:622px;width:500px;color:var(--red);font-size:14px;line-height:1.4}
</style>
</head>
<body>
<div class="spread">

  <section class="page page--left">
    <svg class="page-bg" width="600" height="789" viewBox="0 0 600 789">
      <rect width="600" height="789" fill="var(--navy)"/>
      <path d="M0 520 Q300 440 600 520 L600 789 L0 789 Z" fill="var(--white)"/>
      <path d="M0 532 Q300 452 600 532 L600 789 L0 789 Z" fill="var(--red)"/>
      <path d="M0 544 Q300 464 600 544 L600 789 L0 789 Z" fill="var(--white)"/>
    </svg>
    <div role="img" aria-label="Flock of white Australian White sheep in a yard" style="position:absolute;left:0;top:552px;width:600px;height:212px;background:linear-gradient(160deg,var(--fleece),var(--stone));clip-path:path('M0 0 Q300 -80 600 0 L600 212 L0 212 Z')"></div>
    <div style="position:absolute;left:0;top:764px;width:600px;height:25px;background:var(--red)"></div>

    <div class="kicker">What makes an</div>
    <div class="title-bold">Australian</div>
    <div class="title-light">White?</div>
    <div class="intro">
      <p>The birthplace of the Australian White breed was on the Quenbrook farm in Ardlow Springs, NSW Australia. The original goal of the breed was to provide Australia with a hair sheep breed that thrives under conditions with very little maintenance. They needed to be self replacing, have high fleshing ability, and be consistently uniform. The composite breed is made up of the Poll Dorset, White Dorper, Texel and the Van Rooy. The Australian White breed can now be found on different continents around the world and have done well in various environments.</p>
      <p>This Fall (2018), the Australian White breed will make its debut to the North American continent. Together, Quenbrook and Bricklow Farm are excited to introduce a breed of sheep that is unmatched in terms of meat quality (higher Omega 3s, lower fat melting points, tenderness), efficiency and carcass around the world.</p>
    </div>

    <div class="photo-column" style="left:440px;top:40px;width:152px;height:520px">
      <div class="photo" role="img" aria-label="Two breeders standing with a white ram in a paddock" style="left:10px;top:10px;width:132px;height:160px;background:linear-gradient(180deg,#b9c4c8,var(--grass))"></div>
      <div class="photo" role="img" aria-label="Lamb carcasses hanging in a cool room" style="left:10px;top:178px;width:132px;height:160px;background:linear-gradient(180deg,var(--meat),#b9807a)"></div>
      <div class="photo" role="img" aria-label="Champion ram with ribbon at a show" style="left:10px;top:346px;width:132px;height:164px;background:linear-gradient(180deg,#8a8f86,var(--grass))"></div>
    </div>

    <div class="brand-mark"><span class="square"></span>Quenbrook</div>
  </section>

  <section class="page page--right">
    <svg class="page-bg" width="600" height="789" viewBox="0 0 600 789">
      <rect width="600" height="789" fill="var(--paper)"/>
      <path d="M560 560 Q600 570 600 620 L600 789 L560 789 Z" fill="var(--navy)"/>
      <path d="M0 778 Q300 742 600 782 L600 789 L0 789 Z" fill="var(--red)"/>
      <path d="M10 0 L500 0 L500 440 Q300 450 165 510 Q10 575 10 440 Z" fill="var(--red)"/>
      <path d="M20 0 L490 0 L490 430 Q300 440 160 500 Q20 560 20 440 Z" fill="var(--navy)"/>
    </svg>

    <div class="heading-bold">Breed</div>
    <div class="heading-light">Standards</div>
    <div class="standards">
      <p>The Australian White is a self-replacing, haired sheep with a quiet temperament, high eating quality and low maintenance requirements. They build a thick coat during the winter and their hair becomes much finer during the summer months post shedding.</p>
      <p>The breed reaches mature size early in life creating a more efficient animal.</p>
      <p>Breed goals include the continual focus on eating quality by increasing Omega 3 fatty acids, lower fat melting points, and increased internal marbling to enhance the health benefits, flavor and tenderness of the final product.</p>
    </div>

    <div class="photo-column" style="left:400px;top:120px;width:190px;height:480px">
      <div class="photo" role="img" aria-label="White ram being judged in a show ring" style="left:10px;top:10px;width:170px;height:148px;background:linear-gradient(180deg,#cfcfd4,#7f9a5e)"></div>
      <div class="photo" role="img" aria-label="Handler presenting a ewe at a show" style="left:10px;top:166px;width:170px;height:148px;background:linear-gradient(180deg,#c4c2b8,#8aa062)"></div>
      <div class="photo" role="img" aria-label="Breeders with ribboned sheep at a show" style="left:10px;top:322px;width:170px;height:148px;background:linear-gradient(180deg,#b5b0a6,#7e955a)"></div>
    </div>

    <div class="rams-title">Rams</div>
    <div class="rams-text">A typical ram will have a long, straight top line and a deep body with solid barrel. Average ram mature weights range from 240 to 265 lbs. The ram's head is more masculine with both good breadth and depth, and their pigment tends to be slightly darker than the ewe's. The ram's beam shape also slightly tapers near the shoulders.</div>
  </section>

</div>
</body>
</html>
```